Business card design needed for Automotive Reconditioning business

I have a logo design i just cant decide on the best color or layout for the business card, I will upload all the files so you can see all colors schemes we are considering. I have other file formats if needed let me know.

Target Market(s)

automotive dealerships

Contact Information for Business Card

HERE are the Descriptions and info needed on the card:
Interior Repair: Leather carpet burns panels dash Deoderize
Dealer products and Vin Verify
( spot for name and cell number) My name is Norman Bexley phone 614 352-4180 Title COO www.QuorvalMotive.com

Font styles to use
Sans Serif
Other font styles liked:
• what ever you think looks best

Requirements
Must have
• Must be able to change the name and phone for employees

```html
<!DOCTYPE html>
<html lang="en">
<head>
<meta charset="utf-8">
<title>Quorval Motive Reconditioning Corp. – Business Card</title>
<link rel="stylesheet" href="https://fonts.googleapis.com/css2?family=Exo+2:ital,wght@0,400;0,600;0,800;1,800&display=swap">
<style>
  :root {
    --page-bg: #d9d6d2;
    --card-bg: #1f1f21;
    --card-edge: #2a2a2d;
    --ink-white: #f2f2f2;
    --ink-grey: #b9b9bb;
    --accent-blue: #2e8fd6;
    --divider: #6b6b6e;
  }
  * { margin: 0; padding: 0; box-sizing: border-box; }
  html, body {
    width: 1200px;
    height: 1021px;
    overflow: hidden;
    background: var(--page-bg);
    font-family: "Exo 2", sans-serif;
  }
  .sheet {
    width: 1200px;
    height: 1021px;
    display: flex;
    flex-direction: column;
    align-items: center;
    justify-content: center;
    gap: 40px;
  }
  .card {
    position: relative;
    width: 780px;
    height: 446px;
    background: var(--card-bg);
    border: 1px solid var(--card-edge);
    box-shadow: 0 6px 18px rgba(0,0,0,0.25);
    color: var(--ink-white);
  }

  /* Back side: services */
  .card--back {
    display: flex;
    flex-direction: column;
    align-items: center;
    justify-content: center;
    text-align: center;
  }
  .services__title {
    color: var(--accent-blue);
    font-weight: 800;
    font-size: 22px;
    letter-spacing: 0.5px;
    text-transform: uppercase;
    margin-bottom: 6px;
  }
  .services__list {
    font-weight: 400;
    font-size: 22px;
    line-height: 1.3;
    color: var(--ink-white);
  }

  /* Front side: identity and contact */
  .card--front { padding: 0 70px; }
  .brand {
    position: absolute;
    top: 96px;
    left: 0;
    right: 0;
    text-align: center;
    font-weight: 800;
    color: var(--ink-white);
    text-transform: uppercase;
    line-height: 1.05;
  }
  .brand__name { display: block; font-size: 64px; letter-spacing: 2px; }
  .brand__tagline { display: block; font-size: 24px; letter-spacing: 1.5px; margin-top: 8px; }

  .contact {
    position: absolute;
    left: 110px;
    bottom: 78px;
    display: flex;
    align-items: center;
  }
  .person { text-align: right; padding-right: 28px; }
  .person__name {
    color: var(--accent-blue);
    font-weight: 800;
    font-size: 30px;
    text-transform: uppercase;
    letter-spacing: 0.5px;
  }
  .person__title { font-size: 22px; font-weight: 400; color: var(--ink-white); }
  .contact__divider { width: 2px; height: 62px; background: var(--divider); }
  .details { padding-left: 22px; font-size: 22px; line-height: 1.45; }
  .details__row { display: flex; align-items: center; gap: 10px; }
  .details__icon { width: 20px; height: 20px; flex: none; }
</style>
</head>
<body>
<main class="sheet">

  <section class="card card--back" aria-label="Card back: services">
    <h2 class="services__title">Interior Repair:</h2>
    <p class="services__list">Leather carpet burns panels dash Deoderize<br>Dealer products and Vin Verify</p>
  </section>

  <section class="card card--front" aria-label="Card front: contact">
    <h1 class="brand">
      <span class="brand__name">Quorval Motive</span>
      <span class="brand__tagline">Reconditioning Corp.</span>
    </h1>

    <div class="contact">
      <div class="person">
        <p class="person__name">Norman Bexley</p>
        <p class="person__title">COO</p>
      </div>
      <div class="contact__divider"></div>
      <div class="details">
        <p class="details__row">
          <svg class="details__icon" viewBox="0 0 20 20" aria-hidden="true">
            <rect x="5" y="1.5" width="10" height="17" rx="2" fill="none" stroke="#2e8fd6" stroke-width="1.8"/>
            <line x1="8.5" y1="15.5" x2="11.5" y2="15.5" stroke="#2e8fd6" stroke-width="1.6"/>
          </svg>
          <span>614 352-4180</span>
        </p>
        <p class="details__row">
          <svg class="details__icon" viewBox="0 0 20 20" aria-hidden="true">
            <g fill="none" stroke="#2e8fd6" stroke-width="1.5">
              <circle cx="10" cy="10" r="8.2"/>
              <ellipse cx="10" cy="10" rx="3.6" ry="8.2"/>
              <line x1="1.8" y1="10" x2="18.2" y2="10"/>
              <line x1="3" y1="5.8" x2="17" y2="5.8"/>
              <line x1="3" y1="14.2" x2="17" y2="14.2"/>
            </g>
          </svg>
          <span>www.QuorvalMotive.com</span>
        </p>
      </div>
    </div>
  </section>

</main>
</body>
</html>
```